New webpage for Facility Management Company (cleaning services)

We need a new web page design for a company based in Stockholm, Sweden, called TRV Clean AB (established 1991). We provide cleaning services to the public sector, to businesses, and to home owners. Our services primarily include daily cleaning, floor care, window cleaning, and carpet cleaning.

Our company holds certificates for ISO 9001, ISO 14001, ISO 45001 and "Gnistan".

Referring to "the Swedish model" we honor collective agreements between Verosa (employer-representative organisation and relevant labour unions (e.g. Bärkraft).
The final design should communicate that we are a trustworthy company with a well trained staff, high quality services combined with a commitment to run a sustainable business from a labour and environmental perspective.

DETAILS
General
-----------------------------------------------
• Language: Swedish (we provide text)
• Very important: Easy to administrate for company staff without special technical skills, especially to
o add/change information about HQ staff
o change any text
o add/change information about offered services
• Responsive
• SEO-friendly

Content that web page needs to cover in one way or the other
--------------------------------------------
• Information about our company
• About our staff and contact info to HQstaff/management (photos, contact info)
• Our ambitions and supporting info (quality, environment, labour conditions, certificates, etc)
• Information to customers within the public sector
• Information to customers within the private sector
• Information to customers within the home owner sector
• Services public sector (Swedish = Offentlig sektor)
• Services private business sector (Swedish = Företag) Se berglöf
• Services home owner sector (Swedish=Privat)
• GDPR compliance
• News

Content/Function
-------------------------------
• One specific requirement is that we need a page for information to potentially new employees (some general information and open job positions) with a possibility to fill in a simple application form and upload CV.(Mail?) CAPTCHA or equivalent.
• Contact form for customers with CAPTCHA or equivalent.
• Cookie management
• Integration social media (future); easy to manage/add/delete integration of social media.

We are not interested in a blog at this point of time

```html
<!DOCTYPE html>
<html lang="en">
<head>
<meta charset="utf-8">
<title>TRV Clean AB – A Higher Standard of Clean</title>
<link href="https://fonts.googleapis.com/css2?family=Barlow:wght@300;400;500;600;700&display=swap" rel="stylesheet">
<style>
:root{
  --green:#4cb848;
  --green-dark:#3fa33b;
  --blue:#0a8fdc;
  --blue-deep:#0b7fd0;
  --yellow:#ffd200;
  --ink:#1d1d1d;
  --muted:#555;
  --line:#dcdcdc;
  --footer:#2c2c2c;
  --soft:#f2f4f6;
}
*{box-sizing:border-box;margin:0;padding:0}
html,body{width:1200px;height:4559px;overflow:hidden}
body{font-family:'Barlow',sans-serif;color:var(--ink);background:#fff}
.page{position:relative;width:1200px;height:4559px;overflow:hidden}
.abs{position:absolute}
.btn{position:absolute;background:var(--yellow);color:var(--ink);font-weight:600;font-size:12px;letter-spacing:.3px;border-radius:20px;display:flex;align-items:center;justify-content:center}
.ph{position:absolute}

/* top bar */
.topbar{position:absolute;left:0;top:0;width:1200px;height:30px;background:var(--green);color:#fff;font-size:11px}
.topbar span{position:absolute;top:8px;display:flex;align-items:center;gap:5px}
.dot{width:11px;height:11px;border-radius:50%;background:#fff;display:inline-block}

/* nav */
.nav{position:absolute;top:30px;left:0;width:1200px;height:74px;background:#fff}
.brand{position:absolute;left:84px;top:24px;display:flex;align-items:center;gap:8px;font-size:28px;font-weight:500;color:var(--ink)}
.brand i{width:16px;height:16px;border-radius:50%;background:var(--green);display:block}
.menu{position:absolute;left:425px;top:34px;display:flex;gap:23px;font-size:12.5px;color:var(--ink)}

/* hero */
.hero{position:absolute;top:104px;left:0;width:1200px;height:526px}
.hero h1{position:absolute;left:134px;top:96px;color:#fff;font-size:52px;line-height:64px;font-weight:700}
.hero p{position:absolute;left:134px;top:232px;width:440px;color:#fff;font-size:28px;line-height:36px;font-weight:300}

/* about */
.label{font-size:14px;font-weight:700;color:var(--blue);letter-spacing:.2px}
.about-img{left:134px;top:694px;width:436px;height:469px;border-left:14px solid var(--green)}
.about-h{left:616px;top:724px;width:460px;font-size:25px;line-height:32px;font-weight:500}
.about-p{left:616px;top:842px;width:450px;font-size:12px;line-height:20px;color:#333}
.badges{left:616px;top:1002px;width:452px;height:95px;border-top:1px solid var(--line);border-bottom:1px solid var(--line);display:flex;align-items:center;gap:34px;padding-left:4px}
.badge{width:64px;height:56px;border-radius:50%;background:#dfe9f5}

/* stats */
.stat{position:absolute;top:1235px;width:225px;height:119px;border:1px solid var(--line);border-radius:6px;text-align:center;box-shadow:0 2px 6px rgba(0,0,0,.05)}
.stat b{display:block;margin-top:22px;color:var(--green);font-size:29px;font-weight:400}
.stat span{display:block;font-size:15px;line-height:17px;color:#333;margin-top:2px}

/* services */
.services{position:absolute;top:1411px;left:0;width:1200px;height:437px;background:linear-gradient(90deg,#eef3f7,#e4ecf3 60%,#f3f6f9)}
.svc-h{left:134px;top:120px;width:300px;font-size:29px;line-height:36px;font-weight:500}
.svc-p{left:134px;top:276px;width:300px;font-size:12px;line-height:20px;color:#333}
.svc-card{position:absolute;top:70px;width:190px}
.svc-card .ph{position:relative;height:209px}
.svc-card .foot{height:87px;background:var(--green);color:#fff;text-align:center;padding-top:20px}
.svc-card .foot b{display:block;font-size:15px;font-weight:500;line-height:16px}
.svc-card .foot small{display:block;font-size:11px;margin-top:10px}

/* environment */
.env-h{left:471px;top:1926px;font-size:28px;color:var(--green);font-weight:500}
.env-p{left:471px;top:1978px;width:505px;font-size:18px;line-height:24px;color:#222}

/* industries */
.industries{position:absolute;top:2170px;left:0;width:1200px;height:312px;background:var(--green)}
.ind-h{left:0;top:40px;width:1200px;text-align:center;color:#fff;font-size:30px;font-weight:400}
.ind-p{left:380px;top:92px;width:440px;text-align:center;color:#eaf7e9;font-size:12.5px;line-height:20px}
.ind-card{position:absolute;top:2342px;width:209px;height:182px;background:#fff;border:1px solid var(--line);box-shadow:0 2px 6px rgba(0,0,0,.06)}
.ind-card .ph{position:relative;height:121px}
.ind-card span{display:block;text-align:center;margin-top:20px;font-size:15px;font-weight:500}

/* why */
.why{position:absolute;top:2590px;left:0;width:1200px;height:440px;background:linear-gradient(90deg,#fff 0%,#f4f7fa 40%,#eef2f6 100%)}
.why-h{left:134px;top:2715px;width:300px;font-size:29px;line-height:36px;font-weight:500}
.why-card{position:absolute;width:276px;height:128px;background:#fff;border:1px solid #e6e6e6;box-shadow:0 3px 10px rgba(0,0,0,.08);padding:22px 18px 0 74px}
.why-card svg{position:absolute;left:30px;top:20px}
.why-card b{display:block;font-size:19px;font-weight:500;position:absolute;left:72px;top:22px}
.why-card p{margin-top:28px;font-size:11.5px;line-height:16px;color:#333}

/* testimonial */
.testi{position:absolute;top:3030px;left:0;width:1200px;height:514px;background:var(--blue)}
.testi .lbl{left:0;top:68px;width:1200px;text-align:center;color:#fff;font-size:14px;font-weight:600}
.testi h2{position:absolute;left:285px;top:94px;width:630px;text-align:center;color:#fff;font-size:26px;line-height:32px;font-weight:400}
.tcard{position:absolute;top:3250px;width:400px;height:223px;background:#fff;border-bottom:6px solid var(--green);padding:50px 48px 0}
.tcard p{font-size:12px;line-height:15px;color:#222}
.who{position:absolute;left:48px;top:140px;display:flex;align-items:center;gap:12px;font-size:12px;line-height:14px}
.avatar{width:34px;height:34px;border-radius:50%;background:#cfd5da}

/* quote */
.quote{position:absolute;top:3544px;left:0;width:1200px;height:743px;background:var(--soft)}
.quote h2{position:absolute;left:0;top:52px;width:1200px;text-align:center;font-size:28px;font-weight:400}
.field{position:absolute;background:#fff;border:1px solid #d9d9d9;font-size:11px;color:#999;padding:16px 18px}
.check{position:absolute;width:18px;height:18px;border:1px solid #888;background:#fff}
.verify-mark{position:absolute;left:456px;top:478px;width:30px;height:30px;border-radius:4px;background:#cfd6e0}
.small{position:absolute;font-size:11px;color:#222}
.small a{color:var(--green)}

/* footer */
.footer{position:absolute;top:4287px;left:0;width:1200px;height:272px;background:var(--footer);color:#fff}
.f-brand{position:absolute;left:138px;top:52px;display:flex;align-items:center;gap:8px;font-size:28px;font-weight:500}
.f-brand i{width:16px;height:16px;border-radius:50%;background:#fff;display:block}
.socials{position:absolute;left:140px;top:116px;display:flex;gap:16px}
.socials i{width:16px;height:16px;border-radius:50%;background:#fff;display:block}
.f-col{position:absolute;font-size:11px;line-height:21px}
.f-col h4{font-size:17px;font-weight:400;margin-bottom:16px}
.f-col div{display:flex;align-items:center;gap:6px}
.f-rule{position:absolute;left:134px;top:221px;width:932px;height:1px;background:#555}
.copy{position:absolute;top:238px;left:0;width:1200px;text-align:center;font-size:11px}
</style>
</head>
<body>
<div class="page">

  <div class="topbar">
    <span style="left:140px"><svg width="11" height="12" viewBox="0 0 12 14"><path d="M6 1a4.5 4.5 0 0 0-4.5 4.5C1.5 9 6 13 6 13s4.5-4 4.5-7.5A4.5 4.5 0 0 0 6 1z" fill="none" stroke="#fff" stroke-width="1.3"/><circle cx="6" cy="5.5" r="1.6" fill="#fff"/></svg>Your address here</span>
    <span style="left:740px"><svg width="11" height="11" viewBox="0 0 12 12"><path d="M3 1l2 2.5-1 1.5a7 7 0 0 0 3 3l1.5-1L11 9l-1 2c-5 0-9-4-9-9z" fill="none" stroke="#fff" stroke-width="1.2"/></svg>000-000-00</span>
    <span style="left:836px"><svg width="12" height="10" viewBox="0 0 12 10"><rect x=".6" y=".6" width="10.8" height="8.8" fill="none" stroke="#fff" stroke-width="1.1"/><path d="M1 1l5 4 5-4" fill="none" stroke="#fff" stroke-width="1.1"/></svg>info@website.com</span>
    <span style="left:964px;gap:12px"><i class="dot"></i><i class="dot"></i><i class="dot"></i><i class="dot"></i></span>
  </div>

  <header class="nav">
    <div class="brand"><i></i>TRV Clean AB</div>
    <nav class="menu"><span>Home</span><span>About us ⌄</span><span>Our Service</span><span>Employee ⌄</span><span>Case management</span><span>Contact us ⌄</span><span>News</span></nav>
    <div class="btn" style="left:1003px;top:22px;width:128px;height:34px">GET A QUOTE</div>
  </header>

  <section class="hero">
    <div class="ph" role="img" aria-label="Smiling cleaning team in uniforms and yellow gloves" style="inset:0;background:linear-gradient(90deg,#0a82d6 0%,#2a9be6 38%,#9fcbe8 62%,#d8dde2 100%)"></div>
    <h1>A Higher Standard<br>of Clean</h1>
    <p>Delivering Expert Cleaning &amp; Disinfectionfor Your Facility and Everyone in It</p>
    <div class="btn" style="left:134px;top:377px;width:128px;height:36px">GET A QUOTE</div>
  </section>

  <section>
    <div class="ph about-img" role="img" aria-label="Cleaner holding a bucket of supplies with colleagues behind her" style="background:linear-gradient(135deg,#d9cfc3,#efe9e2 50%,#c9bdb0)"></div>
    <div class="abs label" style="left:616px;top:697px">ABOUT US</div>
    <h2 class="abs about-h">The cleaning company where quality is always higher than price! We have 30 years of experience!</h2>
    <p class="abs about-p">Lorem ipsum dolor sit amet consectetur. Amet volutpat cursus nec non at at lectus sapien placerat. Malesuada sit massa cum eleifend a molestie elementum sed. Commodo at in tempus commodo. Risus interdum dignissim porttitor eu amet. Justo sit amet tortor cras nisl tincidunt. Tincidunt eu eros luctus lectus venenatis facilisis ac.<br>Urna semper fringilla urna metus dignissim et suscipit velit at.</p>
    <div class="abs badges">
      <span class="badge" style="width:118px;border-radius:28px"></span>
      <span class="badge" style="width:78px;border-radius:6px;background:#d7efd5"></span>
      <span class="badge" style="width:56px"></span>
      <span class="badge" style="width:62px;background:#d7efd5"></span>
    </div>
    <div class="btn" style="left:609px;top:1120px;width:137px;height:34px">MORE ABOUT US</div>
  </section>

  <section>
    <div class="stat" style="left:212px"><b>30+</b><span>Years of cleaning<br>experience</span></div>
    <div class="stat" style="left:465px"><b>140+</b><span>Finished Projects</span></div>
    <div class="stat" style="left:718px"><b>20+</b><span style="margin-top:8px">Location Served</span></div>
  </section>

  <section class="services">
    <div class="abs label" style="left:134px;top:81px">OUR SERVICES</div>
    <h2 class="abs svc-h">First Class &amp; Professional Cleaning Service That Fit Your Needs</h2>
    <p class="abs svc-p">Lorem ipsum dolor sit amet consectetur. Sapien mi nibh ipsum augue enim pulvinar. Velit faucibus magna amet vitae mattis</p>
    <div class="svc-card" style="left:464px"><div class="ph" role="img" aria-label="Cleaners vacuuming and dusting a living room" style="background:linear-gradient(160deg,#e9e4dc,#cfc6ba)"></div><div class="foot"><b>Public Sector</b><small>Learn more →</small></div></div>
    <div class="svc-card" style="left:671px"><div class="ph" role="img" aria-label="Cleaner wiping desks in an open office" style="background:linear-gradient(160deg,#dfe6ec,#a9b7c4)"></div><div class="foot"><b>Private Sector</b><small>Learn more →</small></div></div>
    <div class="svc-card" style="left:874px;width:192px"><div class="ph" role="img" aria-label="Two cleaners mopping and wiping in a bright home" style="background:linear-gradient(160deg,#e6ebef,#b8c6cf)"></div><div class="foot" style="padding-top:14px"><b>Home Owner<br>Sector</b><small style="margin-top:6px">Learn more →</small></div></div>
  </section>

  <section>
    <div class="ph" role="img" aria-label="Green tree-shaped city with factories, illustrating environmental care" style="left:186px;top:1890px;width:248px;height:213px;background:radial-gradient(ellipse at 50% 55%,#5eaf3a 0%,#8fc864 45%,rgba(255,255,255,0) 72%)"></div>
    <h2 class="abs env-h">We Think About The Environment</h2>
    <p class="abs env-p">TRV Clean AB strives forenvironmentally friendly cleaning, andwith the right cleaning equipment,chemicals are rarely needed. But in cases whereit is necessary, we choose eco-labelled goods.</p>
  </section>

  <section class="industries">
    <h2 class="abs ind-h">The Industries We Serve</h2>
    <p class="abs ind-p">Lorem ipsum dolor sit amet consectetur. Sapien mi nibh ipsum augue enim pulvinar. Velit faucibus magna amet vitae mattis</p>
  </section>
  <div class="ind-card" style="left:134px"><div class="ph" role="img" aria-label="Modern office lobby" style="background:linear-gradient(160deg,#f1f1f1,#bdbdbd)"></div><span>Office Building</span></div>
  <div class="ind-card" style="left:366px"><div class="ph" role="img" aria-label="School classroom with desks" style="background:linear-gradient(160deg,#e8ecef,#3d5a80)"></div><span>Private Schools</span></div>
  <div class="ind-card" style="left:600px"><div class="ph" role="img" aria-label="Medical equipment in a clinic" style="background:linear-gradient(160deg,#d9e6ec,#1e8aa0)"></div><span>Medical Facilities</span></div>
  <div class="ind-card" style="left:834px"><div class="ph" role="img" aria-label="Furnished home living room" style="background:linear-gradient(160deg,#e6ddd2,#8a7560)"></div><span>Home Service</span></div>

  <section class="why" role="img" aria-label="Faded background of a cleaner wiping a surface"></section>
  <section>
    <div class="abs label" style="left:134px;top:2661px">WHY CHOOSE US</div>
    <h2 class="abs why-h">A Deep Commitment to Quality Cleaning Services</h2>
    <div class="why-card" style="left:464px;top:2650px">
      <svg width="28" height="30" viewBox="0 0 28 30"><rect x="6" y="3" width="16" height="24" rx="2" fill="none" stroke="#4cb848" stroke-width="2.4"/><path d="M10 13h8M10 18h8" stroke="#4cb848" stroke-width="2.4"/></svg>
      <b>Technology</b><p>We utilize state-of-the-art technology to give you a cleaner clean.</p></div>
    <div class="why-card" style="left:779px;top:2650px">
      <svg width="30" height="30" viewBox="0 0 30 30"><circle cx="15" cy="12" r="9" fill="none" stroke="#4cb848" stroke-width="2.4"/><path d="M9 20l-3 8 5-2 3 4 1-6M21 20l3 8-5-2-3 4" fill="none" stroke="#4cb848" stroke-width="2"/></svg>
      <b>Trained Professionals</b><p>Our cleaning crews are trained, professional commercial cleaners.</p></div>
    <div class="why-card" style="left:464px;top:2814px">
      <svg width="32" height="30" viewBox="0 0 32 30"><circle cx="16" cy="6" r="4" fill="#4cb848"/><path d="M4 26c2-6 6-9 12-9s10 3 12 9z" fill="#4cb848"/></svg>
      <b>Customer Care</b><p>Our responsive team proactively serves the needs of every one of our clients.</p></div>
    <div class="why-card" style="left:779px;top:2814px">
      <svg width="32" height="30" viewBox="0 0 32 30"><rect x="3" y="14" width="7" height="14" fill="#4cb848"/><rect x="12.5" y="8" width="7" height="20" fill="#4cb848"/><rect x="22" y="12" width="7" height="16" fill="#4cb848"/></svg>
      <b>Great Results</b><p>We are here to deliver superior service and satisfaction.</p></div>
  </section>

  <section class="testi">
    <div class="abs lbl">TESTIMONIAL</div>
    <h2>Always professional and can be counted on to get the job done. Builds long term relationships to be prosperous together.</h2>
  </section>
  <div class="tcard" style="left:200px"><p>Lorem ipsum dolor sit amet consectetur. Tellus nam vulputate pulvinar malesuada adipiscing sed. Sem natoque sit pretium accumsan integer. Dictumst in molestie in nulla et vitae iaculis.</p><div class="who"><span class="avatar" role="img" aria-label="Portrait of reviewer"></span><span>John Doe<br>Employee at Nordbyte</span></div></div>
  <div class="tcard" style="left:632px"><p>Lorem ipsum dolor sit amet consectetur. Tellus nam vulputate pulvinar malesuada adipiscing sed. Sem natoque sit pretium accumsan integer. Dictumst in molestie in nulla et vitae iaculis.</p><div class="who"><span class="avatar" role="img" aria-label="Portrait of reviewer"></span><span>John Doe<br>Employee at Nordbyte</span></div></div>

  <section class="quote">
    <h2>Request a quote</h2>
    <div class="field" style="left:274px;top:127px;width:312px;height:46px">First name</div>
    <div class="field" style="left:600px;top:127px;width:312px;height:46px">Last name</div>
    <div class="field" style="left:274px;top:189px;width:312px;height:46px">Email Address</div>
    <div class="field" style="left:600px;top:189px;width:312px;height:46px">Phone number</div>
    <div class="field" style="left:274px;top:251px;width:638px;height:46px">Location</div>
    <div class="field" style="left:274px;top:311px;width:638px;height:136px">Message</div>
    <div class="check" style="left:304px;top:485px;width:20px;height:20px"></div>
    <div class="small" style="left:332px;top:488px;font-size:10px">I'm not robot</div>
    <div class="verify-mark" role="img" aria-label="Human verification widget"></div>
    <div class="check" style="left:283px;top:557px"></div>
    <div class="small" style="left:308px;top:559px;font-size:10.5px">I understand that the the information provided by me issubject to the privacy policy</div>
    <div class="small" style="left:282px;top:592px;font-size:10.5px">by sumbitting this form, you agree to the <a>terms</a> and <a>privacy policy</a></div>
    <div class="btn" style="left:269px;top:633px;width:106px;height:36px">SUBMIT</div>
  </section>

  <footer class="footer">
    <div class="f-brand"><i></i>TRV Clean AB</div>
    <div class="socials"><i></i><i></i><i></i><i></i></div>
    <div class="f-col" style="left:506px;top:50px">
      <h4>Contact Us</h4>
      <div><svg width="11" height="12" viewBox="0 0 12 14"><path d="M6 1a4.5 4.5 0 0 0-4.5 4.5C1.5 9 6 13 6 13s4.5-4 4.5-7.5A4.5 4.5 0 0 0 6 1z" fill="none" stroke="#fff" stroke-width="1.3"/></svg>Your address here</div>
      <div><svg width="11" height="11" viewBox="0 0 12 12"><path d="M3 1l2 2.5-1 1.5a7 7 0 0 0 3 3l1.5-1L11 9l-1 2c-5 0-9-4-9-9z" fill="none" stroke="#fff" stroke-width="1.2"/></svg>000-000-00</div>
      <div><svg width="12" height="10" viewBox="0 0 12 10"><rect x=".6" y=".6" width="10.8" height="8.8" fill="none" stroke="#fff" stroke-width="1.1"/><path d="M1 1l5 4 5-4" fill="none" stroke="#fff" stroke-width="1.1"/></svg>info@website.com</div>
    </div>
    <div class="f-col" style="left:752px;top:44px">
      <div>Home</div><div>About us ⌄</div><div>Our Service</div><div>Employee ⌄</div><div>Case management</div><div>Contact us ⌄</div><div>News</div>
    </div>
    <div class="f-rule"></div>
    <div class="copy">©2022 TRV Clean AB</div>
  </footer>

</div>
</body>
</html>
```